Business Card Design Project

Innovative and Elegant. The firm is an Asset Management Firm that will create a series of Investment Vehicles. Should be Bold but modern. Would like a material that is softer than a traditional Buss Card. Like the logos instead of the words (Telephone, email, fax,etc..)
Look attacked for shape and small telephone logos. Don't like their logo, perhaps took small.
Updates

Have Logo and Buss Card projects running simultaneous so please be coordinated since Logo, of course, will be used in the Buss Card design.

Target Market(s)

High Net Worth Individuals

Industry/Entity Type

Business

Font styles to use
Sans Serif

Requirements
Must have
• Shaped with round corners, like a parking ticket.

```html
<!DOCTYPE html>
<html lang="es">
<head>
<meta charset="utf-8">
<title>Mateo Ruiz Delgado — Business Card</title>
<link rel="stylesheet" href="https://fonts.googleapis.com/css2?family=Open+Sans:wght@800&family=Arimo:wght@400&family=Roboto+Condensed:wght@400&display=swap">
<style>
  :root {
    --frame: #333333;
    --paper: #ffffff;
    --ink: #333333;
    --teal: #4aa8b8;
    --sage: #a9baa5;
    --warm: #c9c98a;
  }
  html, body {
    margin: 0;
    padding: 0;
    width: 1200px;
    height: 734px;
    overflow: hidden;
    background: #ffffff;
  }
  .card {
    position: relative;
    width: 1200px;
    height: 734px;
  }
  .card-base, .card-art {
    position: absolute;
    left: 0;
    top: 0;
  }
  .identity-name, .identity-role, .contact-text {
    position: absolute;
    margin: 0;
    line-height: 1;
    white-space: nowrap;
    color: var(--ink);
  }
  .identity-name {
    left: 40px;
    top: 59px;
    font-family: "Open Sans", Arial, sans-serif;
    font-weight: 800;
    font-size: 45px;
  }
  .identity-role {
    left: 43px;
    top: 121px;
    font-family: "Arimo", Arial, sans-serif;
    font-size: 35px;
  }
  .contacts {
    margin: 0;
    padding: 0;
    list-style: none;
  }
  .contact-text {
    left: 84px;
    font-family: "Arimo", Arial, sans-serif;
  }
  .contact-icon {
    position: absolute;
    fill: var(--ink);
  }
  .contact--email .contact-text { top: 195px; font-size: 34px; }
  .contact--address .contact-text { top: 258px; font-size: 30px; font-family: "Roboto Condensed", Arial, sans-serif; }
  .contact--phone .contact-text { top: 309px; font-size: 34px; }
  .contact--mobile .contact-text { top: 352px; font-size: 34px; }
  .contact--web .contact-text { top: 402px; font-size: 31px; }
  .contact--email .contact-icon { left: 18px; top: 199px; width: 40px; height: 24px; }
  .contact--address .contact-icon { left: 22px; top: 246px; width: 30px; height: 35px; }
  .contact--phone .contact-icon { left: 27px; top: 307px; width: 22px; height: 27px; }
  .contact--mobile .contact-icon { left: 27px; top: 352px; width: 22px; height: 34px; }
  .contact--web .contact-icon { left: 26px; top: 405px; width: 31px; height: 31px; }
</style>
</head>
<body>
<div class="card">
  <svg class="card-base" width="1200" height="734" viewBox="0 0 1200 734" aria-hidden="true">
    <rect x="0" y="0" width="1200" height="734" rx="42" fill="var(--frame)"/>
    <rect x="10" y="10" width="1180" height="714" rx="32" fill="var(--paper)"/>
  </svg>

  <svg class="card-art" width="1200" height="734" viewBox="0 0 1200 734" role="img" aria-label="Abstract geometric artwork in teal, yellow and red">
    <defs>
      <linearGradient id="art-field" x1="0.2" y1="0" x2="0.9" y2="1">
        <stop offset="0" stop-color="var(--teal)"/>
        <stop offset="0.55" stop-color="#7fb3ad"/>
        <stop offset="1" stop-color="var(--sage)"/>
      </linearGradient>
      <clipPath id="card-inner">
        <rect x="10" y="10" width="1180" height="714" rx="32"/>
      </clipPath>
    </defs>
    <polygon clip-path="url(#card-inner)" points="664,0 1200,0 1200,734 413,734" fill="url(#art-field)"/>
  </svg>

  <header class="identity">
    <h1 class="identity-name">MATEO RUIZ DELGADO</h1>
    <p class="identity-role">CEO</p>
  </header>

  <ul class="contacts">
    <li class="contact contact--email">
      <svg class="contact-icon" viewBox="0 0 40 24" aria-label="Email"><path d="M0 0h40v4L20 13 0 4z M0 9l20 9 20-9v15H0z"/></svg>
      <span class="contact-text">mateo@valoranta.com</span>
    </li>
    <li class="contact contact--address">
      <svg class="contact-icon" viewBox="0 0 30 35" aria-label="Address"><path d="M15 0L0 14h4v21h8V24h6v11h8V14h4z"/></svg>
      <span class="contact-text">Calle Olmos 2870,PB/ C.A.B.A- Argentina</span>
    </li>
    <li class="contact contact--phone">
      <svg class="contact-icon" viewBox="0 0 22 27" aria-label="Phone"><path d="M4 0c2-1 4 0 5 2l2 5c1 2 0 3-2 4 1 3 3 6 6 8 1-2 3-2 4-1l3 3c1 2 0 4-2 5-3 2-6 1-9-1-5-4-9-10-10-16 0-4 1-7 3-9z"/></svg>
      <span class="contact-text">+54 11 4870-1523</span>
    </li>
    <li class="contact contact--mobile">
      <svg class="contact-icon" viewBox="0 0 22 34" aria-label="Mobile"><path d="M2 0h18v34H2z M4.5 2.5v29h13v-29z"/></svg>
      <span class="contact-text">+54 311 5062-7718</span>
    </li>
    <li class="contact contact--web">
      <svg class="contact-icon" viewBox="0 0 31 31" aria-label="Website"><g fill="none" stroke="var(--ink)" stroke-width="2.4"><circle cx="15.5" cy="15.5" r="13.5"/><ellipse cx="15.5" cy="15.5" rx="5.5" ry="13.5"/><path d="M2 15.5h27M4 9h23M4 22h23"/></g></svg>
      <span class="contact-text">www.valoranta.com</span>
    </li>
  </ul>
</div>
</body>
</html>
```